Tavolint Grab n Go

We have 3 Grab n Go cheese products. Targeting markets, convenience stores, and coffee houses. Same format for all three with some product specific modifications. The label is a wrist watch design. Have uploaded the following: a) die line ai file; b) die line pdf file; c) image of wrist watch label of another grab n go product; d) mockup of three labels in PDF file. Would like a 5 day turnaround.

Target Market(s)

Supermarkets, coffee houses, convenience stores

Other font styles liked:
• "Cheese" should be in a playful font, bold, script (ie - FUGAZ)

Colors

Designer to choose colors to be used in the design.

Requirements
Must have
• Center label area should list the respective components of each SKU
Nice to have
• Straps have colored borders..maybe fruit images.....??

```html
<!DOCTYPE html>
<html lang="en">
<head>
<meta charset="utf-8">
<title>Tavolint Nibblo – Wrist Labels</title>
<link rel="stylesheet" href="https://fonts.googleapis.com/css2?family=Fugaz+One&display=swap">
<style>
  :root {
    --page: #ffffff;
    --strap-edge: #f7941d;
    --strap-hot: #f15a29;
    --strap-core: #6b4123;
    --dial: #6b4123;
    --dial-rim: #4f2d15;
    --brand-yellow: #ffd400;
    --label-white: #ffffff;
    --art-tone: #ffd400;
  }
  html, body {
    margin: 0;
    padding: 0;
    width: 1200px;
    height: 927px;
    overflow: hidden;
    background: var(--page);
  }
  .sheet { display: block; width: 1200px; height: 927px; }
  .strap-text {
    font-family: "Fugaz One", sans-serif;
    font-size: 13px;
    fill: var(--label-white);
  }
  .barcode-slot { font-size: 12px; }
  .brand-name {
    font-family: "Fugaz One", sans-serif;
    font-size: 36px;
    fill: var(--brand-yellow);
  }
  .flavour-line {
    font-family: "Fugaz One", sans-serif;
    font-size: 14px;
    fill: var(--label-white);
  }
  .net-weight {
    font-family: "Fugaz One", sans-serif;
    font-size: 13px;
    fill: var(--brand-yellow);
  }
  .dial { fill: var(--dial); stroke: var(--dial-rim); stroke-width: 2; }
</style>
</head>
<body>
<svg class="sheet" viewBox="0 0 1200 927" xmlns="http://www.w3.org/2000/svg">
  <defs>
    <linearGradient id="strapGradient" x1="67" y1="0" x2="1122" y2="0" gradientUnits="userSpaceOnUse">
      <stop offset="0" stop-color="var(--strap-edge)"/>
      <stop offset="0.13" stop-color="var(--strap-hot)"/>
      <stop offset="0.43" stop-color="var(--strap-core)"/>
      <stop offset="0.58" stop-color="var(--strap-core)"/>
      <stop offset="0.87" stop-color="var(--strap-hot)"/>
      <stop offset="1" stop-color="var(--strap-edge)"/>
    </linearGradient>
    <linearGradient id="artGradient" x1="0" y1="0" x2="1" y2="0">
      <stop offset="0" stop-color="var(--art-tone)" stop-opacity="0.22"/>
      <stop offset="1" stop-color="var(--art-tone)" stop-opacity="0.12"/>
    </linearGradient>
    <path id="weightArc" d="M 514 118 A 80 78 0 0 0 674 118"/>
  </defs>

  <!-- Label 1 -->
  <g class="wrist-label" transform="translate(0,81)">
    <ellipse class="dial" cx="594" cy="108" rx="110" ry="108"/>
    <rect class="strap" x="67" y="41" width="1055" height="134" fill="url(#strapGradient)"/>
    <text class="strap-text" x="80" y="66">Nutrition Facts</text>
    <text class="strap-text" x="80" y="114">Ingredients</text>
    <text class="strap-text" x="204" y="167">Tavolint LLC Los Angeles CA</text>
    <text class="strap-text barcode-slot" transform="translate(1099,108) rotate(-90)" text-anchor="middle">Barcode</text>
    <rect class="flavour-art" x="686" y="45" width="285" height="126" rx="6" fill="url(#artGradient)" role="img" aria-label="Line illustrations of cheese wedges, crackers, grapes, leaves and vinegar bottles"/>
    <text class="brand-name" x="594" y="62" text-anchor="middle">Nibblo</text>
    <text class="flavour-line" x="594" y="106" text-anchor="middle">Balsamic Vinegar</text>
    <text class="flavour-line" x="594" y="124" text-anchor="middle">Artisan Cheese</text>
    <text class="flavour-line" x="594" y="142" text-anchor="middle">Gourmet Crackers</text>
    <text class="net-weight"><textPath href="#weightArc" startOffset="50%" text-anchor="middle">Net Wt 5.5 oz (156g)</textPath></text>
  </g>

  <!-- Label 2 -->
  <g class="wrist-label" transform="translate(0,348)">
    <ellipse class="dial" cx="594" cy="108" rx="110" ry="108"/>
    <rect class="strap" x="67" y="41" width="1055" height="134" fill="url(#strapGradient)"/>
    <text class="strap-text" x="80" y="66">Nutrition Facts</text>
    <text class="strap-text" x="80" y="114">Ingredients</text>
    <text class="strap-text" x="204" y="167">Tavolint LLC Los Angeles CA</text>
    <text class="strap-text barcode-slot" transform="translate(1099,108) rotate(-90)" text-anchor="middle">Barcode</text>
    <rect class="flavour-art" x="700" y="45" width="271" height="126" rx="6" fill="url(#artGradient)" role="img" aria-label="Line illustrations of mangoes, papayas, pineapples, cheese wedges and crackers"/>
    <text class="brand-name" x="594" y="62" text-anchor="middle">Nibblo</text>
    <text class="flavour-line" x="594" y="106" text-anchor="middle">Mango, Papaya, Pineapple</text>
    <text class="flavour-line" x="594" y="124" text-anchor="middle">Artisan Cheese</text>
    <text class="flavour-line" x="594" y="142" text-anchor="middle">Gourmet Crackers</text>
    <text class="net-weight"><textPath href="#weightArc" startOffset="50%" text-anchor="middle">Net Wt 5.5 oz (156g)</textPath></text>
  </g>

  <!-- Label 3 -->
  <g class="wrist-label" transform="translate(0,623)">
    <ellipse class="dial" cx="594" cy="108" rx="110" ry="108"/>
    <rect class="strap" x="67" y="41" width="1055" height="134" fill="url(#strapGradient)"/>
    <text class="strap-text" x="80" y="66">Nutrition Facts</text>
    <text class="strap-text" x="80" y="114">Ingredients</text>
    <text class="strap-text" x="204" y="167">Tavolint LLC Los Angeles CA</text>
    <text class="strap-text barcode-slot" transform="translate(1099,108) rotate(-90)" text-anchor="middle">Barcode</text>
    <rect class="flavour-art" x="690" y="45" width="281" height="126" rx="6" fill="url(#artGradient)" role="img" aria-label="Line illustrations of chocolate pieces, cocoa pods, raspberries, cheese wedges and crackers"/>
    <text class="brand-name" x="594" y="62" text-anchor="middle">Nibblo</text>
    <text class="flavour-line" x="594" y="100" text-anchor="middle">Chocolate Flakes</text>
    <text class="flavour-line" x="594" y="118" text-anchor="middle">Raspberry Sauce</text>
    <text class="flavour-line" x="594" y="136" text-anchor="middle">Artisan Cheese</text>
    <text class="flavour-line" x="594" y="154" text-anchor="middle">Gourmet Crackers</text>
    <text class="net-weight"><textPath href="#weightArc" startOffset="50%" text-anchor="middle">Net Wt 5.5 oz (156g)</textPath></text>
  </g>
</svg>
</body>
</html>
```